TRAVo Kiosk Webpage Design

Just need a simple, single page web design. I have a preliminary idea of what I need, just want to add a professional touch to it. We already have the google map locator plug-in. Generic website is already up and I can send the locator plugin when project is complete for final HTML/CSS Coding. Needs to be coded as a responsive design on a flexible grid (i.e. will auto adjust screen for desktop/tablet/mobile devices)
Target Market(s)
Business/Student/General Public, Mobile Office Kiosk Rental Station (Technology-Printing-Scanning-Faxing, etc...)
Industry/Entity Type
It Professional
Coding
Coded - Design and coding required
Number of Pages Required
1 page
Look and feel
Each slider illustrates characteristics of the customer's brand and the style your logo design should communicate.

```html
<!DOCTYPE html>
<html lang="en">
<head>
<meta charset="utf-8">
<title>TRAVo Kiosk — Mobile Office. Simplified</title>
<link href="https://fonts.googleapis.com/css2?family=Arimo:wght@400;700&family=Lato:wght@400;700&display=swap" rel="stylesheet">
<style>
  :root {
    --brand-blue: #1877b6;
    --button-blue: #1b86c8;
    --header-grey: #dcdde0;
    --logo-tile: #e6e7ea;
    --text-dark: #222;
    --text-body: #333;
    --rule: #e3e3e3;
    --map-base: #e9e5dc;
    --map-water: #8fa9c6;
    --notice-bg: rgba(40,40,40,0.88);
    --footer-top: #1a79b9;
    --footer-bottom: #155f9a;
    --link-blue: #2ea3e6;
  }
  * { box-sizing: border-box; margin: 0; padding: 0; }
  html, body { width: 1200px; height: 983px; overflow: hidden; }
  body { font-family: "Arimo", Arial, sans-serif; background: #fff; color: var(--text-body); position: relative; }

  .site-header { position: absolute; left: 0; top: 0; width: 1200px; height: 148px; background: var(--header-grey); border-bottom: 1px solid #b9bcc1; }
  .brand { position: absolute; left: 500px; top: 0; width: 200px; height: 128px; background: linear-gradient(180deg, var(--logo-tile), var(--header-grey)); text-align: center; }
  .brand-mark { position: absolute; left: 88px; top: 42px; width: 24px; height: 24px; background: var(--brand-blue); border-radius: 50%; }
  .brand-name { position: absolute; left: 0; right: 0; top: 78px; font-size: 17px; color: #1c2a3a; }
  .brand-tagline { position: absolute; left: 0; right: 0; top: 113px; font-size: 12px; color: var(--brand-blue); }

  .intro { position: absolute; left: 100px; top: 214px; width: 1000px; text-align: center; }
  .intro-title { font-size: 35px; font-weight: 400; color: var(--brand-blue); letter-spacing: 0.3px; }
  .intro-text { margin-top: 14px; font-size: 13px; line-height: 22.2px; color: var(--text-body); }
  .locator-title { position: absolute; left: 0; top: 388px; width: 1200px; text-align: center; font-size: 23px; font-weight: 400; color: var(--text-dark); }

  .locator { position: absolute; left: 0; top: 439px; width: 1200px; height: 456px; }
  .map-area { position: absolute; inset: 0; background: linear-gradient(120deg, #ddd6c4 0%, var(--map-base) 35%, #d8d4cc 75%, var(--map-water) 100%); }

  .filter-panel { position: absolute; left: 164px; top: 61px; width: 243px; height: 242px; background: #fff; box-shadow: 0 1px 4px rgba(0,0,0,0.35); padding: 16px 19px; }
  .outlet-count { font-size: 17px; color: var(--text-dark); }
  .show-all { display: block; font-size: 16px; color: var(--brand-blue); margin-top: 3px; text-decoration: none; }
  .filter-select { position: relative; border-top: 1px solid var(--rule); height: 56px; margin-top: 10px; padding-top: 22px; font-size: 13.5px; color: var(--text-dark); }
  .filter-select + .filter-select { margin-top: 0; }
  .filter-select::after { content: ""; position: absolute; right: 10px; top: 28px; border: 5px solid transparent; border-top: 7px solid #999; }
  .select-button { position: absolute; left: 18px; top: 183px; width: 205px; height: 40px; background: var(--button-blue); color: #fff; border: 0; border-bottom: 3px solid #1467a0; font-family: inherit; font-size: 16px; letter-spacing: 0.5px; }

  .search-panel { position: absolute; left: 434px; top: 61px; width: 603px; height: 122px; background: #fff; }
  .search-box { position: absolute; left: 23px; top: 19px; width: 516px; height: 38px; background: #ededed; border: 1px solid #ddd; padding-left: 16px; font-size: 12px; font-style: italic; color: #999; line-height: 38px; }
  .search-icon { position: absolute; right: 12px; top: 11px; }
  .locate-icon { position: absolute; left: 558px; top: 19px; }
  .notice { position: absolute; left: 0; top: 75px; width: 603px; height: 47px; background: var(--notice-bg); color: #fff; font-size: 13.5px; text-align: center; line-height: 47px; padding-right: 30px; letter-spacing: 0.2px; }
  .notice a { color: var(--link-blue); text-decoration: none; }
  .notice-close { position: absolute; right: 11px; top: 9px; width: 28px; height: 28px; background: #111; color: #fff; line-height: 28px; font-size: 18px; padding: 0; }

  .stores-bar { position: absolute; left: 164px; top: 399px; width: 873px; height: 57px; background: #fff; padding: 20px 23px; font-family: "Lato", Arial, sans-serif; font-size: 19px; color: var(--text-dark); }

  .site-footer { position: absolute; left: 0; top: 895px; width: 1200px; height: 88px; background: linear-gradient(180deg, var(--footer-top), var(--footer-bottom)); color: #fff; font-size: 13px; }
  .footer-legal { position: absolute; left: 77px; top: 40px; }
  .footer-contact { position: absolute; left: 889px; top: 28px; line-height: 23px; }
</style>
</head>
<body>
  <header class="site-header">
    <div class="brand">
      <span class="brand-mark"></span>
      <div class="brand-name">TRAVo</div>
      <div class="brand-tagline">SURF/PRINT/SCAN/COPY/FAX</div>
    </div>
  </header>

  <section class="intro">
    <h1 class="intro-title">Mobile Office. Simplified</h1>
    <p class="intro-text">Sed ut perspiciatis unde omnis iste natus error sit voluptatem accusantium doloremque laudantium, totam rem aperiam, eaque ipsa quae ab illo inventore veritatis et quasi architecto beatae vitae dicta sunt explicabo. Nemo enim ipsam voluptatem quia voluptas sit aspernatur aut odit aut fugit, sed quia consequuntur magni dolores eos qui ratione voluptatem sequi nesciunt. Neque porro quisquam est, qui dolorem ipsum quia dolor sit amet, consectetur, adipisci velit, sed quia non numquam eius modi tempora incidunt</p>
  </section>

  <h2 class="locator-title">Locate your nearest TRAVo KIOSK</h2>

  <section class="locator">
    <div class="map-area" role="img" aria-label="Street map of the downtown area showing kiosk locations"></div>

    <div class="filter-panel">
      <div class="outlet-count">0 of 1 outlets</div>
      <a class="show-all" href="#">Show All</a>
      <div class="filter-select">By Region</div>
      <div class="filter-select">Category</div>
      <button class="select-button">SELECT</button>
    </div>

    <div class="search-panel">
      <div class="search-box">Search for nearby stores...
        <svg class="search-icon" width="18" height="18" viewBox="0 0 18 18"><circle cx="7.5" cy="7.5" r="5.5" fill="none" stroke="#333" stroke-width="2.4"/><line x1="11.5" y1="11.5" x2="16" y2="16" stroke="#333" stroke-width="2.6" stroke-linecap="round"/></svg>
      </div>
      <svg class="locate-icon" width="30" height="30" viewBox="0 0 30 30"><circle cx="15" cy="15" r="9" fill="none" stroke="#1b86c8" stroke-width="3"/><circle cx="15" cy="15" r="3" fill="#1b86c8"/><path d="M15 1v7M15 22v7M1 15h7M22 15h7" stroke="#1b86c8" stroke-width="3"/></svg>
      <div class="notice">Location service is not enabled.<a href="#">Continue anyway</a><a href="#">|Share my location</a>
        <button class="notice-close">✕</button>
      </div>
    </div>

    <div class="stores-bar">Stores near you</div>
  </section>

  <footer class="site-footer">
    <div class="footer-legal">Yoursite © 2015&nbsp; Privacy Policy, Terms &amp; condition</div>
    <div class="footer-contact">Question?&nbsp; Feel FREE to Contact us at<br>support@travo-us.com</div>
  </footer>
</body>
</html>
```